Occupational Therapy Clinic Advertisement

Create an advertisement for a magazine. Below I have attached my original ad (Ad 2020.pdf) . I want the ad changed and it should be eye catching. I would like a eye catching graphics added in the ad. It should be a graphic image that applies to education. I am attaching a sample graphic image of that I liked from someone elses ad- it should not be the same- it just is there to show what I like. Please use the same words from my original ad.Dimensions: 3.75in x 10.3 in

Target Market(s)

Parents of School aged children

Requirements
Must have
• Must have eye catching Graphic. Colors should be eye catching for a typed magazine.

```html
<!DOCTYPE html>
<html lang="en">
<head>
<meta charset="utf-8">
<title>Bright Step OT Services</title>
<link rel="stylesheet" href="https://fonts.googleapis.com/css2?family=Questrial&display=swap">
<style>
:root{
  --orange:#f7a23b;
  --orange-light:#fcd96e;
  --blue:#2e78a0;
  --blue-dark:#2a719a;
  --ink:#111;
  --white:#fff;
  --red:#e0262e;
}
*{margin:0;padding:0;box-sizing:border-box}
html,body{width:1200px;height:3341px;overflow:hidden}
body{font-family:"Questrial",sans-serif;color:var(--ink);background:var(--white);position:relative}
.hero-art{position:absolute;left:0;top:0;width:1200px;height:1080px;
  background:
    radial-gradient(ellipse 170px 520px at 600px 480px,rgba(120,90,200,.55) 0%,rgba(60,140,210,.45) 35%,rgba(230,70,140,.35) 65%,rgba(250,210,90,0) 100%),
    radial-gradient(ellipse at 50% 38%,var(--orange-light) 0%,#fbbb46 45%,var(--orange) 85%)}
.cloud{position:absolute;left:0;top:720px;width:1200px;height:420px}
.masthead{position:absolute;left:0;top:945px;width:1200px;text-align:center}
.brand{font-size:104px;color:var(--blue);letter-spacing:3px;line-height:1}
.brand-sub{font-size:56px;line-height:1;margin-top:16px}
.phone-rule{position:absolute;top:1108px;left:0;width:1200px;display:flex;align-items:center;gap:14px;font-size:52px}
.phone-rule .rule{flex:1;height:4px;background:var(--blue)}
.phone-rule .num{display:flex;align-items:center;gap:10px}
.question{position:absolute;left:0;width:1200px;text-align:center;line-height:1.08}
.q-main{top:1192px;font-size:78px}
.q-sub{font-size:60px}
.divider{position:absolute;left:0;width:1200px;height:4px;background:var(--orange)}
.promise{position:absolute;left:0;top:1764px;width:1200px;height:150px;
  background:linear-gradient(90deg,#5aaed2,#88a9a6 50%,#c9a25c);
  color:var(--white);font-size:58px;text-align:center;line-height:68px;padding-top:8px}
.promise .struck{color:var(--ink);position:relative}
.promise .struck::after{content:"";position:absolute;left:-4px;right:-8px;top:50%;height:3px;background:var(--red);transform:rotate(22deg)}
.step{position:absolute;width:440px;height:400px;overflow:visible}
.step svg{width:440px;height:400px;overflow:visible}
.digit{font-family:"Questrial",sans-serif;font-size:330px}
.step-label{position:absolute;height:64px;width:306px;background:var(--orange);font-size:44px;text-align:center;line-height:66px}
.step-text{font-family:"Questrial",sans-serif;font-size:34px;fill:var(--ink)}
.treat-note{position:absolute;left:680px;top:2505px;width:380px;text-align:center;font-size:62px;line-height:1.08}
.info-band{position:absolute;left:0;top:2901px;width:1200px;height:208px;background:var(--blue-dark);color:var(--white);text-align:center}
.info-band .title{font-size:56px;margin-top:16px}
.info-band .line{font-size:41px;line-height:1.3}
.contact-band{position:absolute;left:0;top:3110px;width:1200px;height:145px;background:var(--blue-dark);border-top:3px solid var(--white);color:var(--white);text-align:center;font-size:41px;line-height:1.3;padding-top:18px}
.contact-band .email{color:var(--orange)}
.footer{position:absolute;left:0;top:3255px;width:1200px;height:86px;background:var(--orange);text-align:center;font-size:44px;line-height:90px}
</style>
</head>
<body>
<div class="hero-art" role="img" aria-label="Illustration of a rocket made of colored pencils launching among sketched clouds on an orange background"></div>
<svg class="cloud" viewBox="0 0 1200 420" aria-hidden="true">
  <path d="M0 360 C40 300 120 280 170 270 C190 170 290 150 330 170 C380 80 480 30 600 30 C720 30 800 80 840 160 C900 140 980 170 1010 240 C1080 230 1160 250 1200 270 L1200 420 L0 420 Z" fill="#fff"/>
  <path d="M0 360 C40 300 120 280 170 270 C190 170 290 150 330 170 C380 80 480 30 600 30 C720 30 800 80 840 160 C900 140 980 170 1010 240 C1080 230 1160 250 1200 270" fill="none" stroke="#222" stroke-width="2" stroke-dasharray="10 8"/>
</svg>
<header class="masthead">
  <div class="brand">BRIGHT STEP</div>
  <div class="brand-sub">OT Services</div>
</header>
<div class="phone-rule">
  <span class="rule"></span>
  <span class="num">
    <svg width="58" height="58" viewBox="0 0 56 56" aria-hidden="true"><circle cx="28" cy="28" r="25" fill="none" stroke="#111" stroke-width="3"/><path d="M20 14c-3 2-5 5-3 11 3 8 9 15 16 17 4 1 6-1 8-3l-5-6-4 2c-3-1-7-6-8-9l3-3-3-7z" fill="#111"/></svg>
    (555) 014-227
  </span>
  <span class="rule"></span>
</div>
<p class="question q-main">Does your child struggle<br>with Reading/Kriah?</p>
<div class="divider" style="top:1381px"></div>
<p class="question q-sub" style="top:1405px">Knows the information<br>but fails the test?</p>
<div class="divider" style="top:1565px"></div>
<p class="question q-sub" style="top:1588px">Hasdifficulty remembering<br>names and date?</p>
<div class="promise">YES YOUR CHILD <span class="struck">CAN</span> WILL SUCCEED<br>IN SCHOOL</div>

<svg width="0" height="0" style="position:absolute" aria-hidden="true">
  <defs>
    <linearGradient id="g1" x1="0" y1="0" x2="1" y2="1"><stop offset="0" stop-color="#f8a03a"/><stop offset="1" stop-color="#e8336f"/></linearGradient>
    <linearGradient id="g2" x1="0" y1="0" x2="1" y2="0"><stop offset="0" stop-color="#e8336f"/><stop offset="1" stop-color="#2bb8e0"/></linearGradient>
    <linearGradient id="g3" x1="0" y1="0" x2="1" y2="1"><stop offset="0" stop-color="#2bb8e0"/><stop offset="1" stop-color="#4a4ea0"/></linearGradient>
    <linearGradient id="shade" x1="0" y1="0" x2="1" y2="1"><stop offset="0" stop-color="#8a8a8a"/><stop offset="1" stop-color="#fff" stop-opacity="0"/></linearGradient>
  </defs>
</svg>

<div class="step" style="left:43px;top:1947px">
  <svg viewBox="0 0 440 400">
    <circle cx="240" cy="200" r="180" fill="none" stroke="url(#g1)" stroke-width="7"/>
    <text class="digit" x="30" y="323" fill="none" stroke="url(#g1)" stroke-width="44">1</text>
    <text class="digit" x="30" y="323" fill="#fff" stroke="#fff" stroke-width="30">1</text>
    <path d="M325 125 L430 235 L340 365 L215 260 Z" fill="url(#shade)"/>
    <circle cx="262" cy="200" r="112" fill="#fff"/>
    <text class="step-text" text-anchor="middle" x="255" y="158">Using</text>
    <text class="step-text" text-anchor="middle" x="262" y="202">standardized</text>
    <text class="step-text" text-anchor="middle" x="255" y="246">Evalutions</text>
  </svg>
</div>
<div class="step-label" style="left:131px;top:2350px">We Evaluate</div>

<div class="step" style="left:646px;top:1947px">
  <svg viewBox="0 0 440 400">
    <circle cx="240" cy="200" r="180" fill="none" stroke="url(#g2)" stroke-width="7"/>
    <text class="digit" x="10" y="323" fill="none" stroke="#e8336f" stroke-width="44">2</text>
    <text class="digit" x="10" y="323" fill="#fff" stroke="#fff" stroke-width="30">2</text>
    <path d="M325 110 L430 225 L340 365 L215 250 Z" fill="url(#shade)"/>
    <circle cx="242" cy="192" r="114" fill="#fff"/>
    <text class="step-text" text-anchor="middle" x="240" y="118">Using</text>
    <text class="step-text" text-anchor="middle" x="246" y="162">Reseached</text>
    <text class="step-text" text-anchor="middle" x="240" y="206">based</text>
    <text class="step-text" text-anchor="middle" x="246" y="250">techniques</text>
  </svg>
</div>
<div class="step-label" style="left:716px;top:2350px">We Treat</div>

<div class="step" style="left:39px;top:2413px">
  <svg viewBox="0 0 440 400">
    <circle cx="240" cy="200" r="178" fill="none" stroke="url(#g3)" stroke-width="7"/>
    <text class="digit" x="32" y="323" fill="none" stroke="#2bb8e0" stroke-width="44">3</text>
    <text class="digit" x="32" y="323" fill="#fff" stroke="#fff" stroke-width="30">3</text>
    <path d="M330 125 L430 235 L340 365 L220 260 Z" fill="url(#shade)"/>
    <circle cx="272" cy="200" r="112" fill="#fff"/>
    <text class="step-text" text-anchor="middle" x="235" y="212">6-18</text>
  </svg>
</div>
<div class="step-label" style="left:126px;top:2809px">Ages</div>

<p class="treat-note">We Treat<br>the<br>underlying<br>processing<br>deficits</p>

<section class="info-band">
  <div class="title">Board of OT RSA's accepted</div>
  <div class="line">ocation in orough Park</div>
  <div class="line">Evalution done in borough Park &amp; Staten Isaland</div>
</section>
<section class="contact-band">
  For more information or to be added to our &nbsp;email list<br>
  please email: <span class="email">brightstepot@example.com</span>
</section>
<footer class="footer">Miriam Adler OTR/L..........(555)014-2277</footer>
</body>
</html>
```